QV - menu design

Hi,

We require elegant menu design for upscale restaurant. Please find attached the logo and the menu items for your reference.

for inspiration, this is a good website: -
http://www.platewhisper.example/bellfoldnotes/about.php

We are very much open for Menu Size suggestions.

unfortunately the place is going under renovation, we don't have updated images to it. the closest look and feel to our place is http://varnelo.example ..

we are also open for creative options on the shape, the styles, etc. as long as it represents the fine dine feel ...

Thanks ...

Dear All,

We wouldlike to extend our apology for not being able to provide feedbacks on everysingle design. We were extremely busy and we have multiple contests opensimultaneously which makes the process even harder.

However,we would like to thank you all for the efforts you have put into designingour menu. It is very much appreciated …

We wishyou all success in your design ventures and we are quite positive that we willbe working with many of you on many projects in the soon future. 

Thanks & Regards,

TLG Team...

 

 

 

Industry/Entity Type

Restaurant

Requirements
Must have
• Please ensure that there are 'some' images in the menu ... this is very important.
Should not have
• IMPORTANT: -

1. Please DO NOT insert any currency sign to the menu
2. Please keep the prices of the menu at the end of the menu items descriptions NOT beside the menu item names. The font of the price should be similar to the menu item description and please DO NOT bold the numbers. the prices should be subtle.

Thank you ...

```html
<!DOCTYPE html>
<html lang="en">
<head>
<meta charset="utf-8">
<title>QV – Menu Cover</title>
<link rel="stylesheet" href="https://fonts.googleapis.com/css2?family=Michroma&family=Josefin+Sans:wght@400&display=swap">
<style>
  :root {
    --backdrop: #e6e6e6;
    --cover: #2a2829;
    --cover-shade: #232122;
    --fold: #1a1919;
    --ink: #ffffff;
    --tan: #b08a62;
  }
  * { margin: 0; padding: 0; box-sizing: border-box; }
  html, body {
    width: 1200px;
    height: 712px;
    overflow: hidden;
    background: var(--backdrop);
  }
  .canvas {
    position: relative;
    width: 1200px;
    height: 712px;
  }
  .spread {
    position: absolute;
    left: 178px;
    top: 184px;
    width: 854px;
    height: 420px;
    display: flex;
  }
  .panel {
    position: relative;
    width: 427px;
    height: 100%;
    background: var(--cover);
  }
  .panel--back {
    background: linear-gradient(90deg, var(--cover) 0%, var(--cover) 85%, var(--cover-shade) 100%);
  }
  .panel--front {
    background: linear-gradient(90deg, var(--cover-shade) 0%, var(--cover) 18%, var(--cover) 100%);
    border-left: 1px solid var(--fold);
  }
  .wordmark {
    position: absolute;
    text-align: center;
    color: var(--ink);
    font-family: "Michroma", sans-serif;
    font-weight: 400;
    line-height: 1;
  }
  .wordmark__name {
    display: block;
    font-size: 22px;
    letter-spacing: 5px;
  }
  .wordmark__kind {
    display: block;
    margin-top: 8px;
    font-size: 8px;
    letter-spacing: 6px;
  }
  .panel--back .wordmark {
    left: 0;
    width: 427px;
    top: 350px;
  }
  .panel--front .wordmark {
    left: 0;
    width: 436px;
    top: 214px;
  }
  .panel--front .wordmark__name { font-size: 26px; letter-spacing: 6px; }
  .panel--front .wordmark__kind { font-size: 9px; letter-spacing: 7px; }
  .menu-tab {
    position: absolute;
    left: 175px;
    bottom: 0;
    width: 83px;
    height: 38px;
    background: var(--tan);
    color: var(--ink);
    font-family: "Josefin Sans", sans-serif;
    font-size: 20px;
    letter-spacing: 1px;
    display: flex;
    align-items: center;
    justify-content: center;
    padding-top: 4px;
  }
</style>
</head>
<body>
  <main class="canvas">
    <section class="spread">
      <div class="panel panel--back">
        <div class="wordmark">
          <span class="wordmark__name">QUILL VALE</span>
          <span class="wordmark__kind">CAFÉ</span>
        </div>
      </div>
      <div class="panel panel--front">
        <div class="wordmark">
          <span class="wordmark__name">QUILL VALE</span>
          <span class="wordmark__kind">CAFÉ</span>
        </div>
        <div class="menu-tab">MENU</div>
      </div>
    </section>
  </main>
</body>
</html>
```